Need creative website for award-winning author

I need someone to create a cool website for indie award-winning author Lorna Quibb. Right now she one young adult novel and a published short story. The site should appeal to both adults and children. The site has to needs to be available through PEXLOFT's platform.

HOME Page
About Lorna
Bio
Books
Community Projects
Appearances
Blogs & Videos
Contact
Store

Check out the following author's websites:
Mark Tilden
Sarah Kwell
Hazel Brnok
Dale Fenwright
Rick Abernath

Target Market(s)

Readers (all ages)

Industry/Entity Type

Adult

Coding

Coded - Design and coding required

Number of Pages Required

5+ page

Requirements
Must have
• Cutting edge look

```html
<!DOCTYPE html>
<html lang="en">
<head>
<meta charset="utf-8">
<title>Lorna Quibb — Author</title>
<link href="https://fonts.googleapis.com/css2?family=Rajdhani:wght@500;600&family=Oswald:wght@300;400&family=Open+Sans:wght@300&family=Hind:wght@600&display=swap" rel="stylesheet">
<style>
:root{
  --hero-top:#4b4847;
  --hero-bottom:#3a3736;
  --ink-light:#f4f2f0;
  --nav-grey:#c9c5c2;
  --accent-yellow:#f2c200;
  --button-purple:#9b6fd0;
  --band-top:#55305f;
  --band-bottom:#3b1f48;
  --band-text:#b9a0c6;
  --gold-ring:#b48a3a;
  --footer-bg:#2f2d2d;
  --footer-text:#8f8b88;
  --icon-grey:#9a9694;
}
*{margin:0;padding:0;box-sizing:border-box}
html,body{width:1200px;height:1002px;overflow:hidden;background:var(--hero-bottom)}
.page{position:relative;width:1200px;height:1002px;overflow:hidden}

.hero{position:absolute;left:0;top:0;width:1200px;height:646px;overflow:hidden;
  background:linear-gradient(180deg,var(--hero-top),var(--hero-bottom))}
.city-backdrop{position:absolute;left:0;top:190px;width:780px;height:330px;
  background:linear-gradient(180deg,rgba(255,255,255,0) 0%,rgba(255,255,255,.06) 55%,rgba(255,255,255,0) 100%);
  -webkit-mask-image:linear-gradient(90deg,#000 60%,transparent);mask-image:linear-gradient(90deg,#000 60%,transparent)}
.social{position:absolute;display:flex;gap:4px}
.social span{width:21px;height:21px;border-radius:50%;background:var(--icon-grey)}
.hero .social{right:42px;top:20px}

.brand{position:absolute;left:44px;top:60px;font-family:"Rajdhani",sans-serif;font-weight:500;
  font-size:42px;line-height:1;color:var(--accent-yellow);white-space:nowrap}

.main-nav{position:absolute;left:36px;top:160px;width:202px;list-style:none}
.main-nav li{border-top:1px dotted rgba(255,255,255,.22);text-align:center;white-space:nowrap;
  font-family:"Oswald",sans-serif;font-weight:300;font-size:21px;line-height:32px;
  color:var(--nav-grey);text-transform:uppercase}
.main-nav li:first-child{border-top:none}
.main-nav li.current{color:var(--accent-yellow)}

.intro{position:absolute;left:319px;top:214px;width:392px;font-family:"Rajdhani",sans-serif;
  font-weight:600;font-size:20px;line-height:24px;color:var(--ink-light)}
.intro p+p{margin-top:24px}
.bio-button{position:absolute;left:319px;top:461px;width:197px;height:43px;border-radius:6px;
  background:var(--button-purple);color:#fff;font-family:"Hind",sans-serif;font-weight:600;
  font-size:17px;line-height:45px;text-align:center;box-shadow:0 6px 8px rgba(0,0,0,.3)}

.portrait{position:absolute;left:777px;top:113px;width:420px;height:420px;border:4px solid var(--accent-yellow);
  border-radius:10px;transform:rotate(15deg);
  background:linear-gradient(180deg,#4f7a3a 0%,#3a5a2e 40%,#1f2c5a 70%,#1a2450 100%);
  box-shadow:0 18px 20px rgba(0,0,0,.35)}

.features{position:absolute;left:0;top:646px;width:1200px;height:318px;
  background:linear-gradient(180deg,var(--band-top),var(--band-bottom));
  box-shadow:inset 0 8px 10px -6px rgba(0,0,0,.45)}
.feature{position:absolute;left:0;top:0}
.feature > *{position:absolute}
.book-cover{width:110px;height:171px;background:linear-gradient(160deg,#cfe4f2,#3c8dc4 55%,#1d4f86);
  box-shadow:2px 3px 6px rgba(0,0,0,.4)}
.round-photo{width:104px;height:104px;border-radius:50%;border:5px solid var(--gold-ring);
  background:linear-gradient(180deg,#d9d3cc,#8e7e72)}
.feature-body{top:50px}
.feature h2{font-family:"Rajdhani",sans-serif;font-weight:600;font-size:23px;line-height:24px;color:var(--ink-light);white-space:nowrap}
.feature p{margin-top:0;font-family:"Open Sans",sans-serif;font-weight:300;font-size:14px;line-height:20.7px;color:var(--band-text)}
.cta{top:238px;display:flex;align-items:center;gap:11px;white-space:nowrap;font-family:"Oswald",sans-serif;
  font-weight:400;font-size:17px;line-height:28px;color:var(--ink-light);text-transform:uppercase}
.divider{position:absolute;top:48px;width:1px;height:143px;background:rgba(255,255,255,.3)}

.site-footer{position:absolute;left:0;top:964px;width:1200px;height:38px;background:var(--footer-bg)}
.site-footer small{position:absolute;left:16px;top:9px;font-family:"Rajdhani",sans-serif;font-weight:500;
  font-size:15px;color:var(--footer-text);white-space:nowrap}
.site-footer .social{right:14px;top:8px}
.site-footer .social span{width:22px;height:22px}
</style>
</head>
<body>
<div class="page">
  <header class="hero">
    <div class="city-backdrop" role="img" aria-label="Faint city skyline backdrop"></div>
    <div class="social"><span></span><span></span><span></span><span></span></div>
    <div class="brand">Lorna Quibb</div>
    <ul class="main-nav">
      <li class="current">Home</li>
      <li>About Lorna</li>
      <li>Books</li>
      <li>Community Projects</li>
      <li>Appearances</li>
      <li>Blogs &amp; Videos</li>
      <li>Contact</li>
      <li>Store</li>
    </ul>
    <div class="intro">
      <p>Lorna Quibb is an indie award-winning author. As a child growing up in New Orleans, Lorna Quibb developed her lifelong love for storytelling while exchanging pen-pal letters with her cousin in California.</p>
      <p>"Paper Kites" is her first published novel, partly inspired by her daughter's experience on a new neighborhood swim team.</p>
    </div>
    <div class="bio-button">Lorna Quibb's Bio</div>
    <div class="portrait" role="img" aria-label="Portrait photo of Lorna Quibb"></div>
  </header>

  <section class="features">
    <article class="feature">
      <div class="book-cover" style="left:30px;top:54px" role="img" aria-label="Cover of the novel Paper Kites"></div>
      <div class="feature-body" style="left:158px;width:240px">
        <h2>Paper Kites</h2>
        <p>"Paper Kites" is a contemporary middle-grade novel that explores the lives of military children. The book delves into themes of sports, race, community, and volunteerism as a way of supporting families through difficult times.</p>
      </div>
      <div class="cta" style="left:159px">
        <svg width="28" height="28" viewBox="0 0 30 30"><circle cx="15" cy="15" r="13.5" fill="none" stroke="#fff" stroke-width="2"/><path d="M8 15h13M16 10l5 5-5 5" fill="none" stroke="#fff" stroke-width="2"/></svg>Buy Now
      </div>
    </article>
    <div class="divider" style="left:401px"></div>

    <article class="feature">
      <div class="round-photo" style="left:419px;top:52px" role="img" aria-label="Photo of Lorna Quibb at a community event"></div>
      <div class="feature-body" style="left:540px;width:245px">
        <h2>Community Projects</h2>
        <p>Lorem ipsum dolor sit amet, consecte tuer adipiscing elit, sed diam nonum my nibh euismod tincidunt ut laoreet dolore magna aliquam erat volutpat. Ut wisi enim ad minim veniam, quis nostrud exerci tation ullamcorper sus cipit lobortis nisl ut aliquip ex ea.</p>
      </div>
      <div class="cta" style="left:541px">
        <svg width="28" height="28" viewBox="0 0 30 30"><circle cx="15" cy="15" r="13.5" fill="none" stroke="#fff" stroke-width="2"/><path d="M8 15h13M16 10l5 5-5 5" fill="none" stroke="#fff" stroke-width="2"/></svg>Learn More
      </div>
    </article>
    <div class="divider" style="left:800px"></div>

    <article class="feature">
      <div class="round-photo" style="left:817px;top:52px" role="img" aria-label="Photo of Lorna Quibb speaking at an appearance"></div>
      <div class="feature-body" style="left:937px;width:245px">
        <h2>Appearances</h2>
        <p>Lorem ipsum dolor sit amet, consecte tuer adipiscing elit, sed diam nonum my nibh euismod tincidunt ut laoreet dolore magna aliquam erat volutpat. Ut wisi enim ad minim veniam, quis nostrud exerci tation ullamcorper sus cipit lobortis nisl ut aliquip ex ea.</p>
      </div>
      <div class="cta" style="left:937px">
        <svg width="28" height="28" viewBox="0 0 30 30"><circle cx="15" cy="15" r="13.5" fill="none" stroke="#fff" stroke-width="2"/><path d="M8 15h13M16 10l5 5-5 5" fill="none" stroke="#fff" stroke-width="2"/></svg>Learn More
      </div>
    </article>
  </section>

  <footer class="site-footer">
    <small>© 2017 Lorna Quibb. All Rights Reserved.</small>
    <div class="social"><span></span><span></span><span></span><span></span></div>
  </footer>
</div>
</body>
</html>
```